Real Estate Listing Landing Page

I am looking for a landing page for my Flat Fee MLS Listing website... The name of my website is "Brightkey Home Sales".

I am a big fan of this landing page setup and would like something similar.
https://quaylinehomes.com/

I am a fan of the design style on https://quaylinehomes.com/ and also this design style as well... https://2817.velmontedge.com/

Use your creativity and incorporate your own twists that you would feel lift up this landing pages' appeal. I'd love some red color incorporated within the design.

Target Market(s)

Real Estate Home Sellers

Industry/Entity Type

Real Estate

Coding

Coded - Design and coding required

Font styles to use
Sans Serif

Colors
0054AA
0677BA
7BADD7
CADEEF
E8F1F8
0094D4
00A9DD
6FCCEA
C7EBF8
E9F6FB
EB3D1F
EC4F4E
F09395
F8D3D4
FCEDEE

```html
<!DOCTYPE html>
<html lang="en">
<head>
<meta charset="utf-8">
<title>Brightkey Home Sales</title>
<link href="https://fonts.googleapis.com/css2?family=Poppins:ital,wght@0,400;0,500;0,600;0,700;1,300&display=swap" rel="stylesheet">
<style>
:root{
  --red:#eb1c2d;
  --red-soft:#f8d3d4;
  --ink:#222;
  --text:#555;
  --muted:#777;
  --light:#f4f4f4;
  --line:#e3e3e3;
  --dark:#1f1f1f;
  --footer:#262626;
}
*{box-sizing:border-box;margin:0;padding:0}
html,body{width:1200px;height:3909px;overflow:hidden}
body{font-family:'Poppins',sans-serif;color:var(--ink);background:#fff;position:relative}
.abs{position:absolute}
.brand-name{font-weight:600;font-size:34px;line-height:1;color:#333}
.brand-tag{font-size:17px;color:var(--red);margin-top:4px}
.social{display:flex;gap:34px}
.social span{width:24px;height:24px;border-radius:50%;background:var(--red);display:block}
.hero{top:80px;left:0;width:1200px;height:692px;background:linear-gradient(100deg,#f4f2ef 0%,#d8dde3 35%,#b9c3cd 55%,#eef0f2 75%,#dfe5ea 100%)}
.hero-photo{position:absolute;inset:0;background:radial-gradient(ellipse 260px 180px at 470px 360px,rgba(140,150,165,.55),transparent),radial-gradient(ellipse 120px 200px at 990px 330px,rgba(225,170,140,.6),transparent)}
.nav{top:137px;left:215px;display:flex;gap:38px;font-size:16px;font-weight:500;color:#222}
.btn-outline{border:2px solid var(--red);color:#222;font-size:16px;display:flex;align-items:center;justify-content:center;background:transparent}
.account{top:116px;left:974px;width:131px;height:45px;color:var(--red);border-radius:3px}
.hero h1{top:330px;left:92px;font-size:66px;line-height:64px;font-weight:600;color:#111}
.hero h1 em{font-style:normal;color:var(--red);display:block}
.hero-copy{top:483px;left:89px;font-size:22px;line-height:27px;color:#111;width:450px}
.learn{top:586px;left:87px;width:130px;height:51px}
.about{top:772px;left:0;width:1200px;height:639px;background:var(--light)}
.section-title{font-size:29px;font-weight:500;color:#333;letter-spacing:.3px}
.about-copy{font-size:15px;line-height:19px;color:#666;width:460px}
.read{top:1231px;left:107px;width:131px;height:51px}
.steps-title{top:1485px;width:1200px;text-align:center;left:-20px}
.step-label{font-size:19px;font-weight:500;color:#555}
.step-circle{width:108px;height:108px;border-radius:50%;border:2px solid var(--red);background:#fff;display:flex;align-items:center;justify-content:center}
.btn-red{background:var(--red);color:#fff;font-size:17px;display:flex;align-items:center;justify-content:center;border-radius:2px}
.card{width:316px;height:415px;border:1px solid var(--line);border-radius:6px;background:#fff;box-shadow:0 2px 10px rgba(0,0,0,.05);text-align:center}
.card .tag{position:absolute;top:18px;right:18px;background:var(--red);color:#fff;font-size:12px;padding:3px 7px;border-radius:3px}
.card h3{font-size:19px;font-weight:400;margin-top:42px;color:#333}
.card p.desc{font-size:13px;line-height:20px;color:#888;margin:8px 28px 0}
.price{margin-top:18px;font-size:28px;color:var(--red)}
.price small{font-size:13px;color:#888;margin-left:8px}
.features{list-style:none;text-align:left;margin:20px 0 0 28px;font-size:14px;color:#777}
.features li{margin-bottom:16px;display:flex;align-items:center;gap:8px}
.card .btn-red{width:146px;height:48px;margin:16px auto 0}
.testimonials{top:2587px;left:0;width:1200px;height:539px;background:var(--light)}
.avatar{width:114px;height:114px;border-radius:50%;border:3px solid #fff;box-shadow:0 0 0 2px var(--red);background:linear-gradient(160deg,#8a97a6,#3f4954)}
.stars{color:#f29b1e;font-size:13px;letter-spacing:1px;text-align:center}
.tname{font-size:16px;font-weight:600;letter-spacing:1px;color:#333;text-align:center}
.quote{font-size:17px;line-height:23px;font-style:italic;font-weight:300;color:#888;letter-spacing:1px;width:320px}
.mini-social{display:flex;gap:30px}
.mini-social span{width:16px;height:16px;border-radius:50%;background:var(--red);display:block}
.dot{width:15px;height:15px;border-radius:50%;background:var(--red)}
.newsletter{top:3155px;left:0;width:1200px;height:451px;background:linear-gradient(120deg,#2a2a2a,#1b1b1b 50%,#2b2a29)}
.newsletter h2{top:3233px;width:1200px;left:-10px;text-align:center;color:var(--red);font-size:29px;font-weight:600}
.news-copy{top:3320px;left:230px;width:720px;text-align:center;color:#ddd;font-size:16px;line-height:20px}
.field{top:3431px;left:263px;width:418px;height:55px;background:#fff;border:1px solid #ccc;color:#999;font-size:21px;letter-spacing:2px;display:flex;align-items:center;padding-left:68px}
.subscribe{top:3431px;left:681px;width:257px;height:55px;font-size:21px;letter-spacing:2px}
.footer{top:3606px;left:0;width:1200px;height:303px;background:var(--footer)}
.f-title{color:var(--red);font-size:15px;font-weight:600;text-decoration:underline}
.f-item{color:#fff;font-size:15px;line-height:18px}
.badge{background:#d8dff0;border-radius:3px}
</style>
</head>
<body>

<header>
  <div class="abs" style="top:12px;left:50px">
    <div class="brand-name">Real Estate</div>
    <div class="brand-tag">Flat Fee MLS Listing</div>
  </div>
  <div class="abs social" style="top:28px;left:874px" aria-label="Social links">
    <span></span><span></span><span></span><span></span>
  </div>
</header>

<section class="abs hero">
  <div class="hero-photo" role="img" aria-label="Hand holding a small red toy house with keys, blurred house in the background"></div>
</section>
<nav class="abs nav"><span>Home</span><span>About Us</span><span>Sell</span><span>Sold</span><span>Package</span><span>Review</span><span>Contact Us</span></nav>
<div class="abs btn-outline account">Account</div>
<h1 class="abs hero" style="top:330px;left:92px;width:auto;height:auto;background:none;font-size:66px;line-height:64px;font-weight:600;color:#111">Welcome to<em style="font-style:normal;color:var(--red);display:block">Real Estate</em></h1>
<p class="abs hero-copy">Lorem ipsum dolor sit amet, consecte-<br>tur adipiscing elit, sed do eiusmod</p>
<div class="abs btn-outline learn">Learn More</div>

<section class="abs about"></section>
<h2 class="abs section-title" style="top:942px;left:107px">ABOUT US</h2>
<div class="abs about-copy" style="top:1017px;left:107px">
  <p>Lorem ipsum dolor sit amet, consectetur adipiscing elit, sed do eiusmod tempor incididunt ut labore et dolore magna aliqua. Quis ipsum suspendisse ultrices gravida. Risus commodo viverra maecenas accumsan lacus vel facilisis.</p>
  <p style="margin-top:14px">Lorem ipsum dolor sit amet, consectetur adipiscing elit, sed do eiusmod tempor incididunt ut labore et dolore magna aliqua. Quis ipsum suspendisse ultrices gravida. Risus commodo viverra maecenas accumsan lacus vel facilisis.</p>
</div>
<div class="abs btn-outline read">Read More</div>
<svg class="abs" style="top:895px;left:660px" width="460" height="450" viewBox="0 0 460 450">
  <circle cx="225" cy="222" r="222" fill="var(--red)"/>
  <circle cx="210" cy="227" r="210" fill="#fff"/>
  <circle cx="212" cy="228" r="200" fill="#c9d2dc"/>
</svg>
<div class="abs" role="img" aria-label="Model house with keys on architectural plans" style="top:923px;left:672px;width:400px;height:400px;border-radius:50%;background:radial-gradient(circle at 45% 40%,#7a3a38 0%,#5b6a80 35%,#d7dde4 70%,#eef0f2 100%)"></div>

<h2 class="abs section-title steps-title">STEPS FOR STELLING HOME</h2>
<svg class="abs" style="top:1600px;left:360px" width="470" height="280" viewBox="0 0 470 280" aria-hidden="true">
  <path d="M10 140 Q 70 10 230 5 Q 390 10 455 140" fill="none" stroke="#7a8696" stroke-width="2"/>
  <line x1="8" y1="215" x2="8" y2="275" stroke="#ddd"/><line x1="455" y1="215" x2="455" y2="275" stroke="#ddd"/>
</svg>
<div class="abs step-circle" style="top:1729px;left:311px"><svg width="54" height="50" viewBox="0 0 54 50" fill="none" stroke="#777" stroke-width="2"><circle cx="10" cy="10" r="5"/><circle cx="44" cy="10" r="5"/><rect x="18" y="3" width="18" height="12"/><path d="M4 48V24h12v24M50 48V24H38v24M16 30h22"/></svg></div>
<div class="abs step-circle" style="top:1587px;left:430px"><svg width="54" height="50" viewBox="0 0 54 50" fill="none" stroke="#777" stroke-width="2"><circle cx="10" cy="10" r="5"/><circle cx="44" cy="10" r="5"/><rect x="18" y="3" width="18" height="12"/><path d="M4 48V24h12v24M50 48V24H38v24M16 30h22"/></svg></div>
<div class="abs step-circle" style="top:1587px;left:645px"><svg width="54" height="50" viewBox="0 0 54 50" fill="none" stroke="#777" stroke-width="2"><circle cx="10" cy="10" r="5"/><circle cx="44" cy="10" r="5"/><rect x="18" y="3" width="18" height="12"/><path d="M4 48V24h12v24M50 48V24H38v24M16 30h22"/></svg></div>
<div class="abs step-circle" style="top:1729px;left:763px"><svg width="54" height="50" viewBox="0 0 54 50" fill="none" stroke="#777" stroke-width="2"><circle cx="10" cy="10" r="5"/><circle cx="44" cy="10" r="5"/><rect x="18" y="3" width="18" height="12"/><path d="M4 48V24h12v24M50 48V24H38v24M16 30h22"/></svg></div>
<span class="abs step-label" style="top:1776px;left:206px">Heading 1</span>
<span class="abs step-label" style="top:1614px;left:323px">Heading 2</span>
<span class="abs step-label" style="top:1614px;left:766px">Heading 3</span>
<span class="abs step-label" style="top:1776px;left:885px">Heading 4</span>
<div class="abs" style="top:1756px;left:440px;width:307px;text-align:center;font-size:38px;font-weight:600;color:#333">Real Estate</div>
<div class="abs btn-red" style="top:1840px;left:529px;width:129px;height:47px">View More</div>

<h2 class="abs section-title" style="top:2022px;left:534px">PACKAGE</h2>
<div class="abs card" style="top:2110px;left:107px">
  <span class="tag">Monthly</span><h3>Monthly</h3>
  <p class="desc">Lorem Ipsum is simply dummy text of the printing and typesetting industry.</p>
  <div class="price">$39.00<small>/ Monthly</small></div>
  <ul class="features"><li>✓ Install a Patio or Pathway</li><li>✓ Install Landscaping</li><li>✓ Waterproof a Deck Costs</li><li>✓ Remove a Tree Stump</li></ul>
  <div class="btn-red">Get started</div>
</div>
<div class="abs card" style="top:2113px;left:448px">
  <span class="tag">Monthly</span><h3>Monthly</h3>
  <p class="desc">Lorem Ipsum is simply dummy text of the printing and typesetting industry.</p>
  <div class="price">$39.00<small>/ Monthly</small></div>
  <ul class="features"><li>✓ Install a Patio or Pathway</li><li>✓ Install Landscaping</li><li>✓ Waterproof a Deck Costs</li><li>✓ Remove a Tree Stump</li></ul>
  <div class="btn-red">Get started</div>
</div>
<div class="abs card" style="top:2112px;left:790px">
  <span class="tag">Monthly</span><h3>Monthly</h3>
  <p class="desc">Lorem Ipsum is simply dummy text of the printing and typesetting industry.</p>
  <div class="price">$39.00<small>/ Monthly</small></div>
  <ul class="features"><li>✓ Install a Patio or Pathway</li><li>✓ Install Landscaping</li><li>✓ Waterproof a Deck Costs</li><li>✓ Remove a Tree Stump</li></ul>
  <div class="btn-red">Get started</div>
</div>

<section class="abs testimonials"></section>
<h2 class="abs section-title" style="top:2664px;left:486px">TESTIMONIALS</h2>
<div class="abs avatar" role="img" aria-label="Client portrait" style="top:2802px;left:117px"></div>
<div class="abs stars" style="top:2932px;left:117px;width:114px">★★★★★</div>
<div class="abs tname" style="top:2956px;left:107px;width:134px">Sam Rowe</div>
<p class="abs quote" style="top:2818px;left:272px">Lorem ipsum dolor sit amet, con-sectetur adipiscing elit, sed do ei-usmod tempor incididunt ut labore et dolore magna aliqua. Quis ipsum suspendisse ultrices</p>
<div class="abs mini-social" style="top:2968px;left:349px"><span></span><span></span><span></span><span></span></div>
<div class="abs avatar" role="img" aria-label="Client portrait" style="top:2802px;left:662px"></div>
<div class="abs stars" style="top:2932px;left:662px;width:114px">★★★★★</div>
<div class="abs tname" style="top:2958px;left:652px;width:134px">Sam Rowe</div>
<p class="abs quote" style="top:2811px;left:806px">Lorem ipsum dolor sit amet, con-sectetur adipiscing elit, sed do ei-usmod tempor incididunt ut labore et dolore magna aliqua. Quis ipsum suspendisse ultrices</p>
<div class="abs mini-social" style="top:2968px;left:894px"><span></span><span></span><span></span><span></span></div>
<div class="abs dot" style="top:3051px;left:583px"></div>
<div class="abs dot" style="top:3051px;left:619px"></div>
<div class="abs dot" style="top:3051px;left:651px;background:transparent;border:2px solid #333"></div>

<section class="abs newsletter" role="img" aria-label="Dark photo of a handshake over a desk"></section>
<h2 class="abs newsletter" style="height:auto;background:none;top:3233px">SUBSCRIBE OUR NEWSLETTER</h2>
<p class="abs news-copy">Lorem ipsum dolor sit amet, consectetur adipiscing elit, sed do eiusmod tempor in-cididunt ut labore et dolore magna aliqua. Quis ipsum suspendisse ultrices gravida. Risus commodo viverra maecenas accumsan lacus vel facilisis.</p>
<div class="abs field">Your Email Here</div>
<div class="abs btn-red subscribe">Subscribe</div>

<footer class="abs footer"></footer>
<div class="abs" style="top:3660px;left:202px">
  <div class="brand-name" style="color:#fff">Real Estate</div>
  <div class="brand-tag">Flat Fee MLS Listing</div>
</div>
<div class="abs badge" style="top:3750px;left:205px;width:120px;height:48px" aria-label="Listing partner badge"></div>
<div class="abs" style="top:3808px;left:205px;width:64px;height:56px;border:3px solid #555;border-radius:4px" aria-label="Housing badge"></div>
<div class="abs f-title" style="top:3650px;left:518px">CONTACT US</div>
<svg class="abs" style="top:3703px;left:518px" width="32" height="32" viewBox="0 0 32 32" fill="none" stroke="#fff" stroke-width="2"><circle cx="16" cy="16" r="14"/><path d="M11 9l3 3-2 2q2 4 6 6l2-2 3 3-2 3q-8-1-12-11z"/></svg>
<div class="abs f-item" style="top:3710px;left:563px">CALL US<br>0123 456 789</div>
<svg class="abs" style="top:3764px;left:518px" width="32" height="32" viewBox="0 0 32 32" fill="none" stroke="#fff" stroke-width="2"><circle cx="16" cy="16" r="14"/><rect x="9" y="11" width="14" height="10"/><path d="M9 11l7 6 7-6"/></svg>
<div class="abs f-item" style="top:3767px;left:563px">EMAIL US<br>hello@brightkeymail.com</div>
<svg class="abs" style="top:3822px;left:518px" width="32" height="34" viewBox="0 0 32 34" fill="none" stroke="#fff" stroke-width="2"><circle cx="16" cy="17" r="14"/><path d="M16 27s-6-7-6-11a6 6 0 0112 0c0 4-6 11-6 11z"/><circle cx="16" cy="16" r="2"/></svg>
<div class="abs f-item" style="top:3825px;left:563px">Dummy Address Here,<br>Address Here</div>
<div class="abs f-title" style="top:3655px;left:880px">QUICK LINK</div>
<div class="abs f-item" style="top:3712px;left:885px;line-height:32px;font-size:16px">Sell<br>Sold<br>Package<br>Review<br>Contact Us</div>

</body>
</html>
```